Marcus Pellow Physical Therapy and Wellness
One-on-one care. Tailored recovery. Lasting strength
Marcus Pellow Physical Therapy and Wellness  -
Modern Professional Simple
Dr. Marcus Pellow, PT, DPT
4375 K Street NW Washington, DC 20016
mkp@marcuspellowPT.example
www.marcuspellowPT.example

```html
<!DOCTYPE html>
<html lang="en">
<head>
<meta charset="utf-8">
<title>Marcus Pellow Physical Therapy and Wellness — Stationery Package</title>
<link rel="stylesheet" href="https://fonts.googleapis.com/css2?family=Josefin+Sans:wght@400;600&display=swap">
<style>
  :root {
    --bg-light: #d6e01f;
    --bg-dark: #a7bb12;
    --green-light: #7bb32a;
    --green-mid: #4f8f1c;
    --green-deep: #2c6410;
    --paper: #ffffff;
    --brand-orange: #d9731c;
    --ink-green: #3d6b12;
    --label-yellow: #f3f38a;
    --rule: #e9a35a;
  }
  * { box-sizing: border-box; margin: 0; padding: 0; }
  html, body { width: 1200px; height: 921px; overflow: hidden; }
  body {
    font-family: "Josefin Sans", sans-serif;
    background: radial-gradient(ellipse at 40% 40%, var(--bg-light) 0%, var(--bg-dark) 100%);
    position: relative;
  }
  .piece { position: absolute; box-shadow: 0 10px 24px rgba(60, 80, 0, 0.28); }

  .brand { display: flex; flex-direction: column; align-items: center; text-align: center; }
  .brand-row { display: flex; align-items: center; gap: 8px; }
  .brand-dot { width: 14px; height: 14px; border-radius: 50%; background: var(--green-mid); flex: none; }
  .brand-name { font-weight: 600; text-transform: uppercase; letter-spacing: 2px; color: var(--brand-orange); white-space: nowrap; }
  .brand-tagline { font-size: 7px; letter-spacing: 0.5px; text-transform: uppercase; color: var(--ink-green); margin-top: 4px; white-space: nowrap; }
  .brand--on-green .brand-name { color: var(--paper); }
  .brand--on-green .brand-dot { background: var(--label-yellow); }
  .brand--on-green .brand-tagline { color: #e8f2c8; }

  .folder {
    left: 60px; top: 110px; width: 360px; height: 520px; border-radius: 4px 14px 14px 4px;
    background: radial-gradient(circle at 50% 30%, var(--green-light) 0%, var(--green-mid) 45%, var(--green-deep) 100%);
    padding-top: 60px;
  }
  .folder .brand-name { font-size: 18px; }

  .letterhead {
    left: 460px; top: 110px; width: 360px; height: 510px; background: var(--paper);
    padding: 34px 30px;
  }
  .letterhead .brand-name { font-size: 15px; }
  .letterhead-footer {
    position: absolute; left: 30px; right: 30px; bottom: 28px;
    border-top: 1px solid var(--rule); padding-top: 8px;
    font-size: 8px; color: var(--brand-orange); text-align: center; letter-spacing: 0.4px; line-height: 1.6;
  }

  .envelope {
    left: 60px; top: 680px; width: 440px; height: 200px; background: var(--paper); padding: 22px 24px;
  }
  .envelope .brand { align-items: flex-start; text-align: left; }
  .envelope .brand-name { font-size: 13px; }
  .envelope-return { font-size: 8px; color: var(--ink-green); margin-top: 10px; line-height: 1.5; }

  .card { width: 270px; height: 160px; left: 880px; }
  .card--front {
    top: 110px;
    background: radial-gradient(circle at 30% 40%, var(--green-light), var(--green-deep));
    display: flex; align-items: center; justify-content: center;
  }
  .card--front .brand-name { font-size: 15px; }
  .card--back { top: 300px; background: var(--paper); padding: 22px 22px; }
  .card--back .brand { align-items: flex-start; text-align: left; }
  .card--back .brand-name { font-size: 12px; }
  .card-person { font-size: 12px; font-weight: 600; color: var(--ink-green); margin-top: 16px; }
  .card-details { font-size: 8px; color: var(--ink-green); line-height: 1.6; margin-top: 6px; }
  .card-stripe { position: absolute; left: 0; right: 0; bottom: 0; height: 10px; background: var(--green-mid); }

  .package { position: absolute; left: 880px; top: 515px; width: 290px; }
  .package .brand { align-items: flex-start; text-align: left; }
  .package .brand-name { font-size: 20px; }
  .package-title { color: var(--label-yellow); font-size: 15px; margin-top: 34px; }
  .package-subtitle { color: var(--label-yellow); font-size: 15px; margin-top: 16px; }
  .package-list { list-style: none; color: var(--label-yellow); font-size: 15px; margin-top: 18px; line-height: 1.45; }
  .package-list li::before { content: "• "; }
</style>
</head>
<body>

  <section class="piece folder" aria-label="Presentation folder">
    <div class="brand brand--on-green">
      <div class="brand-row"><span class="brand-dot"></span><span class="brand-name">Marcus Pellow</span></div>
      <p class="brand-tagline">One-on-one care. Tailored recovery. Lasting strength</p>
    </div>
  </section>

  <section class="piece letterhead" aria-label="Letterhead">
    <div class="brand">
      <div class="brand-row"><span class="brand-dot"></span><span class="brand-name">Marcus Pellow</span></div>
      <p class="brand-tagline">One-on-one care. Tailored recovery. Lasting strength</p>
    </div>
    <footer class="letterhead-footer">
      4375 K Street NW Washington, DC 20016<br>
      mkp@marcuspellowPT.example &nbsp;|&nbsp; www.marcuspellowPT.example
    </footer>
  </section>

  <section class="piece envelope" aria-label="Envelope">
    <div class="brand">
      <div class="brand-row"><span class="brand-dot"></span><span class="brand-name">Marcus Pellow</span></div>
      <p class="brand-tagline">Physical Therapy and Wellness</p>
    </div>
    <p class="envelope-return">4375 K Street NW Washington, DC 20016</p>
  </section>

  <section class="piece card card--front" aria-label="Visiting card front">
    <div class="brand brand--on-green">
      <div class="brand-row"><span class="brand-dot"></span><span class="brand-name">Marcus Pellow</span></div>
      <p class="brand-tagline">Physical Therapy and Wellness</p>
    </div>
  </section>

  <section class="piece card card--back" aria-label="Visiting card back">
    <div class="brand">
      <div class="brand-row"><span class="brand-dot"></span><span class="brand-name">Marcus Pellow</span></div>
    </div>
    <p class="card-person">Dr. Marcus Pellow, PT, DPT</p>
    <p class="card-details">
      4375 K Street NW Washington, DC 20016<br>
      mkp@marcuspellowPT.example<br>
      www.marcuspellowPT.example
    </p>
    <span class="card-stripe"></span>
  </section>

  <aside class="package">
    <div class="brand">
      <div class="brand-row"><span class="brand-dot"></span><span class="brand-name">Marcus Pellow</span></div>
      <p class="brand-tagline">One-on-one care. Tailored recovery. Lasting strength</p>
    </div>
    <p class="package-title">Stationery Package</p>
    <p class="package-subtitle">Items Included:</p>
    <ul class="package-list">
      <li>Visiting Card</li>
      <li>Visiting Card Back</li>
      <li>Letterhead</li>
      <li>Envelope</li>
    </ul>
  </aside>

</body>
</html>
```